IT Product Event Invitations

We are requesting the design of two invitations for a series of technological events that will be held between the company Tidewell Core and its partner in the Dominican Republic, Velorbit.
Both events represent the launch of the Tidewell Core brand in the Dominican Republic.
The first event is an elegant dinner aimed at the banking sector of the Dominican Republic to showcase the "Ledgerline Banking Suite" software.
Event information:
- Descriptive text for the invitation: Velorbit y Tidewell Core le invitan a descubrir cómo reducir costos, aumentar la automatización y mejorar la satisfacción de los clientes a través de una solución única para enfrentar los desafíos de la banca.
- Date: 25 de Septiembre
- Time: 7PM
- Location: El Mirtal, Av. Julio Benavente 318
In the invitation, consider using the colors of the Tidewell Core and Velorbit brands if possible. You can find the logos in the webpage
The second event is a wine tasting to present "Crestway Operations Hub" aimed at various industries.
Event information:
- Descriptive text for the invitation: Velorbit y Tidewell Core le invitan a conocer una solución que le permitirá a toda su empresa brindar una experiencia de servicio a otro nivel.
- Date: 26 de Septiembre
- Time: 7PM
In the invitation, consider using the colors of the Tidewell Core and Velorbit brands if possible. You can find the logos in the web page.
Both invitations must have a button for participant registration and that when you click on the image, it will direct you to a form.
Form for Ledgerline Banking Suite: https://signup.palvento-forms.example/event/k3rq9-banking-dinner-7xw2
Form for Crestway Operations Hub: https://signup.palvento-forms.example/event/m8vt4-wine-tasting-2jq5
Target Market(s)
Enterprise Customers
Industry/Entity Type
Technology
Look and feel
Each slider illustrates characteristics of the customer's brand and the style your logo design should communicate.

```html
<!DOCTYPE html>
<html lang="es">
<head>
<meta charset="utf-8">
<title>Invitación a cena — Velorbit y Tidewell Core</title>
<link rel="stylesheet" href="https://fonts.googleapis.com/css2?family=Roboto:wght@400;500;700;900&display=swap">
<style>
  :root {
    --navy: #15294a;
    --peach: #f7d6a8;
    --orange: #f0a050;
    --red: #e8372a;
    --green: #5fd35a;
    --ink: #111111;
    --white: #ffffff;
    --stage: #e9eef0;
  }
  * { margin: 0; padding: 0; box-sizing: border-box; }
  html, body { width: 1200px; height: 1200px; overflow: hidden; background: var(--stage); font-family: "Roboto", Arial, sans-serif; }
  .invitation {
    position: absolute; left: 0; top: 251px; width: 1200px; height: 698px;
    background: var(--navy); overflow: hidden;
  }
  .artwork { position: absolute; inset: 0; width: 1200px; height: 698px; }
  .brand {
    position: absolute; top: 34px; display: flex; align-items: center; gap: 8px;
    font-weight: 700; font-size: 25px; color: var(--white); letter-spacing: 0.5px;
  }
  .brand--velorbit { left: 300px; }
  .brand--velorbit .brand-dot { width: 24px; height: 24px; border-radius: 50%; background: var(--red); }
  .brand--tidewell { left: 752px; font-weight: 500; }
  .intro {
    position: absolute; left: 284px; top: 114px; width: 320px; text-align: center;
    font-size: 15.5px; line-height: 23.5px; color: var(--ink);
  }
  .intro strong { font-weight: 500; }
  .event-card {
    position: absolute; left: 619px; top: 168px; width: 260px; text-align: center; color: var(--white);
  }
  .event-title { font-weight: 700; font-size: 31px; line-height: 32px; letter-spacing: 0.3px; }
  .event-date { font-weight: 700; font-size: 18.5px; line-height: 23px; margin-top: 4px; }
  .event-venue { font-weight: 700; font-size: 18.5px; line-height: 23px; }
  .event-address { font-weight: 400; font-size: 12.5px; line-height: 18px; }
  .rsvp {
    position: absolute; left: 661px; top: 588px; width: 220px; height: 77px;
    display: flex; align-items: center; justify-content: center;
    font-weight: 900; font-size: 39px; color: var(--ink); text-decoration: none; letter-spacing: 1px;
  }
</style>
</head>
<body>
<main class="invitation">
  <svg class="artwork" viewBox="0 0 1200 698" aria-hidden="false">
    <defs>
      <linearGradient id="warm" x1="0" y1="0" x2="1" y2="0.3">
        <stop offset="0" stop-color="#f0a050"/>
        <stop offset="1" stop-color="#e8372a"/>
      </linearGradient>
      <linearGradient id="warmRev" x1="0" y1="0.2" x2="1" y2="0.8">
        <stop offset="0" stop-color="#e8372a"/>
        <stop offset="0.55" stop-color="#e8372a"/>
        <stop offset="1" stop-color="#f29a6a"/>
      </linearGradient>
      <linearGradient id="teamTone" x1="0" y1="0" x2="1" y2="1">
        <stop offset="0" stop-color="#235d70"/>
        <stop offset="1" stop-color="#10304a"/>
      </linearGradient>
      <linearGradient id="venueTone" x1="0" y1="0" x2="1" y2="1">
        <stop offset="0" stop-color="#4a5a30"/>
        <stop offset="1" stop-color="#3b2a1c"/>
      </linearGradient>
      <linearGradient id="dishTone" x1="1" y1="0" x2="0" y2="1">
        <stop offset="0" stop-color="#ececec"/>
        <stop offset="0.6" stop-color="#b9aea4"/>
        <stop offset="1" stop-color="#2a211b"/>
      </linearGradient>
    </defs>

    <!-- peach message band -->
    <rect class="message-band" x="0" y="97" width="1200" height="176" fill="var(--peach)"/>

    <!-- backdrop circle behind event card -->
    <circle cx="910" cy="253" r="61" fill="url(#warmRev)"/>

    <!-- dashed path lines -->
    <path d="M 640 85 C 600 160, 600 300, 640 360 C 670 380, 700 372, 720 370" fill="none" stroke="var(--orange)" stroke-width="1.5" stroke-dasharray="5 4"/>
    <path d="M 720 370 C 760 440, 700 520, 620 560 C 560 590, 480 560, 420 580" fill="none" stroke="var(--green)" stroke-width="1.5" stroke-dasharray="5 4"/>
    <path d="M 320 520 C 350 560, 400 560, 440 560" fill="none" stroke="var(--green)" stroke-width="1.5" stroke-dasharray="5 4"/>

    <!-- team photo area -->
    <path role="img" aria-label="Fotografía de tres profesionales de negocios sobre fondo verde azulado"
          d="M 318 273 L 662 273 C 690 340, 655 425, 560 482 C 480 528, 398 546, 340 512 C 294 482, 292 380, 318 273 Z"
          fill="url(#teamTone)" stroke="var(--white)" stroke-width="2"/>

    <!-- sparkle -->
    <path d="M 527 296 Q 531 320 555 324 Q 531 328 527 352 Q 523 328 499 324 Q 523 320 527 296 Z" fill="var(--green)"/>

    <!-- venue photo area -->
    <ellipse role="img" aria-label="Fotografía de la entrada del restaurante con vegetación de noche"
             cx="402" cy="626" rx="74" ry="76" fill="url(#venueTone)" stroke="var(--white)" stroke-width="2"/>

    <!-- dish photo area -->
    <path role="img" aria-label="Fotografía de un plato gourmet servido"
          d="M 520 512 C 560 500, 610 560, 632 610 C 650 650, 590 668, 540 676 C 490 684, 466 650, 472 600 C 478 555, 490 520, 520 512 Z"
          fill="url(#dishTone)" stroke="var(--white)" stroke-width="2"/>

    <!-- event card blob -->
    <path d="M 720 76 C 780 70, 860 150, 890 238 C 914 310, 830 360, 720 362 C 640 364, 612 310, 618 220 C 624 130, 660 82, 720 76 Z"
          fill="url(#warm)" stroke="var(--white)" stroke-width="2.5"/>

    <!-- floating circles -->
    <circle cx="243" cy="558" r="35" fill="url(#warm)"/>
    <circle cx="769" cy="480" r="42" fill="url(#warm)"/>

    <!-- dots -->
    <circle cx="222" cy="178" r="7" fill="var(--orange)"/>
    <circle cx="215" cy="238" r="7" fill="var(--red)"/>
    <circle cx="269" cy="307" r="7" fill="var(--red)"/>
    <circle cx="224" cy="422" r="7" fill="var(--red)"/>
    <circle cx="255" cy="453" r="7" fill="var(--green)"/>
    <circle cx="905" cy="140" r="7" fill="var(--green)"/>
    <circle cx="834" cy="353" r="7" fill="var(--orange)"/>
    <circle cx="709" cy="547" r="7" fill="var(--green)"/>
    <circle cx="854" cy="537" r="7" fill="var(--red)"/>
    <circle cx="305" cy="671" r="7" fill="var(--green)"/>

    <!-- rsvp button shape -->
    <path d="M 661 602 Q 661 588 675 588 L 881 588 Q 880 640 838 665 L 675 665 Q 661 665 661 651 Z"
          fill="var(--green)" stroke="var(--white)" stroke-width="2"/>
  </svg>

  <div class="brand brand--velorbit"><span class="brand-dot"></span>Velorbit</div>
  <div class="brand brand--tidewell">Tidewell Core</div>

  <p class="intro">
    <strong>Velorbit y Tidewell Core<br>
    le invitan a descubrir cómo reducir<br>
    costos, aumentar la automatización</strong><br>
    y mejorar la satisfacción de los clientes<br>
    a través de una solución única para<br>
    enfrentar los desafíos de la banca.
  </p>

  <div class="event-card">
    <h1 class="event-title">INVITACIÓN<br>A CENA</h1>
    <p class="event-date">25 de Septiembre, 7pm</p>
    <p class="event-venue">El Mirtal,</p>
    <p class="event-address">Av. Julio Benavente 318</p>
  </div>

  <a class="rsvp" href="https://signup.palvento-forms.example/event/k3rq9-banking-dinner-7xw2">RSVP</a>
</main>
</body>
</html>
```